Business Card Design

Hi we are an MMA and fitness gym, we would like a design similar to the themes in the logo provided and with all the information on it as well.
Updates

1. The phone number is 0455 612 907
2. The address is 18 Calloway street

Hi some of the designs have the wrong phone number the correct number is 0417 583 640

the correct address is 18 Calloway Street 

Industry/Entity Type

Fitness

Contact Information for Business Card

Danielle Fairow
Club Manager
0417 583 640
18 Calloway Street Wynnum Central
Qld 4178
gym@ironvalemma.com.au
www.ironvalemma.com.au

MMA, Boxing, Muay Thai, Kids MMA, BlazeRun group fitness

```html
<!DOCTYPE html>
<html lang="en">
<head>
<meta charset="utf-8">
<title>Iron Vale MMA Gym – Business Card</title>
<link rel="stylesheet" href="https://fonts.googleapis.com/css2?family=Tinos:wght@400;700&display=swap">
<style>
  :root {
    --ink: #000000;
    --paper: #ffffff;
    --mist: #b9c5c0;
    --pine: #3b7360;
    --accent: #e0186e;
    --echo: #9a9a9a;
    --badge-text: #d4d4d4;
  }
  html, body {
    margin: 0;
    padding: 0;
    overflow: hidden;
  }
  .card {
    position: relative;
    width: 1200px;
    height: 686px;
    overflow: hidden;
    background: linear-gradient(180deg, var(--paper) 0%, var(--paper) 12%, var(--mist) 52%, var(--pine) 100%);
    font-family: "Tinos", "Times New Roman", serif;
    color: var(--ink);
  }
  .brand-badge {
    position: absolute;
    left: 32px;
    top: 0;
    width: 311px;
    height: 383px;
    background: var(--ink);
    display: flex;
    align-items: center;
    justify-content: center;
  }
  .brand-badge__name {
    font-weight: 700;
    font-size: 44px;
    letter-spacing: 3px;
    color: var(--badge-text);
    margin-top: -70px;
  }
  .gym-title {
    position: absolute;
    left: 360px;
    top: 140px;
    width: 810px;
    height: 130px;
  }
  .gym-title text {
    font-family: "Tinos", "Times New Roman", serif;
    font-weight: 700;
    font-size: 96px;
  }
  .gym-title__echo {
    fill: var(--echo);
    opacity: 0.8;
  }
  .gym-title__main {
    fill: var(--accent);
    stroke: var(--ink);
    stroke-width: 2.5px;
    paint-order: stroke;
  }
  .services {
    position: absolute;
    left: 360px;
    top: 292px;
    width: 810px;
    margin: 0;
    text-align: center;
    font-size: 26px;
    line-height: 34px;
    letter-spacing: 1px;
  }
  .services span {
    display: block;
  }
  .details {
    position: absolute;
    left: 11px;
    top: 423px;
    width: 1178px;
    height: 240px;
    box-sizing: border-box;
    border: 3px solid var(--ink);
    display: flex;
  }
  .details__block {
    box-sizing: border-box;
    padding: 22px 14px 0 13px;
    font-size: 41px;
    line-height: 53px;
    white-space: nowrap;
  }
  .details__block--person {
    width: 611px;
    border-right: 4px solid var(--ink);
  }
  .details__block--contact {
    flex: 1;
    font-size: 34px;
    line-height: 50px;
  }
  .details__line {
    display: block;
  }
</style>
</head>
<body>
  <main class="card">
    <div class="brand-badge">
      <span class="brand-badge__name">IRON VALE</span>
    </div>

    <svg class="gym-title" viewBox="0 0 810 130" aria-label="Iron Vale MMA Gym">
      <text class="gym-title__echo" x="12" y="100" textLength="795" lengthAdjust="spacingAndGlyphs">IRON VALE MMA GYM</text>
      <text class="gym-title__main" x="2" y="82" textLength="795" lengthAdjust="spacingAndGlyphs">IRON VALE MMA GYM</text>
    </svg>

    <p class="services">
      <span>MMA · BOXING · MUAY THAI · KIDS MMA</span>
      <span>BLAZERUN GROUP FITNESS</span>
    </p>

    <section class="details">
      <div class="details__block details__block--person">
        <span class="details__line">DANIELLE FAIROW</span>
        <span class="details__line">CLUB MANAGER</span>
        <span class="details__line">0417 583 640</span>
      </div>
      <div class="details__block details__block--contact">
        <span class="details__line">18 CALLOWAY STREET</span>
        <span class="details__line">WYNNUM CENTRAL QLD 4178</span>
        <span class="details__line">gym@ironvalemma.com.au</span>
        <span class="details__line">www.ironvalemma.com.au</span>
      </div>
    </section>
  </main>
</body>
</html>
```